Brochure Design - ICT Company

We are an ICT (Information & Communication Technologies) company and need a brochure design. Our main products and services are Office Equipment, Banking Equipment, Software Solutions, IT Hardware, Networking & Communication, Audio Video Solutions and Social Media Marketing. Please check our website www.tovanelix.com for details in our Solutions menu.

Designs should include colors from our website (blue) and our logo (orange/green) in the best possible combination with lighter colors. Graphics and patterns should be sleek and modern. Brochure size to be square shaped (21 cm x 21 cm).

Final design should portray us as a futuristic technology company.

Provide a design with sample images and we can purchase them if required. Alternatively, let us know if the images from our website will suffice.
Updates

Project Deadline Extended
Reason: Awaiting more designs and more creativity. If any input is required from us, do inform asap.

Uploaded 2 sample brochure designs that we found interesting - looking for more inspiring ideas.

Thanks

Hi everyone, the following text should appear on the cover of the brochure design:

'Your One Stop Solution Provider for Information & Communication Technologies'

Project Deadline Extended
Reason: Awaiting management feedback - might require changes in design. Open to receiving more designs.

Thank you all for participating. Received many creative ideas and will be back with more requests. 

Target Market(s)

Decision Makers in UAE: IT Managers, Purchase Manager, CEO, Finance Managers etc

Industry/Entity Type

Communication

Requirements
Must have
• We have 7 divisions within our company. Brochure should dedicate 2 pages to each company - Text on one side and Image on the other.

7 divisions are: (details on website)
Office Equipment - sales of copiers, fax etc to any industry, any size office
Banking Equipment - sales of coin counters, counterfeit detectors etc to banks and foreign exchange houses
IT & Communication - providing server, email, software licenses to any industry, any size office
Software Solution - Quillon partner + provide software solution to any industry, any size company
ELV & Security - provide CCTV, security systems to big companies, warehouses etc any industry
AV & Convergence - provide latest technology multi sensory solutions for theatres, opera houses, education sector, hospitality sector, medical sector etc.
Social Media Marketing - provide marketing options to companies through social media (www.tovanesphere.com)

Images to be used in the brochure are attached - they are concept images associated with each division. The design for the inner pages can be created around this basic image.

Cover page - design with logo, 'An Information & Technologies Company'
Back page - Design with address details
Inner sections:
1. About Us
2. Seven divisions as described above

The pattern for the text for inner pages should be:
Heading describing problem
Small Paragraph text describing solution
Small inset images of the

Nice to have
• Modern, sleek look with images that reflect an ICT/IT company - stand out from the regular brochure design
Should not have
• The design should not use old-style design, fonts etc.

```html
<!DOCTYPE html>
<html lang="en">
<head>
<meta charset="utf-8">
<title>Tovane Technologies – Brochure Cover Spread</title>
<link href="https://fonts.googleapis.com/css2?family=Questrial&display=swap" rel="stylesheet">
<style>
  :root {
    --orange: #e86d1f;
    --green: #5e9a2e;
    --dark-green: #1f5a2a;
    --navy: #1c3f8c;
    --line-blue: #1e2f6b;
    --band-grey: #9a9a9a;
    --banner-black: rgba(0,0,0,0.88);
    --deep-blue: #0f2a5c;
    --white: #ffffff;
  }
  * { margin: 0; padding: 0; box-sizing: border-box; }
  html, body { width: 1200px; height: 600px; overflow: hidden; background: var(--white); }
  body { font-family: "Questrial", "Century Gothic", sans-serif; position: relative; }

  .spread { position: relative; width: 1200px; height: 600px; }

  /* back page contact block */
  .contact { position: absolute; left: 29px; top: 57px; width: 120px; }
  .contact h3 { color: var(--orange); font-size: 9px; font-weight: 400; margin-bottom: 1px; }
  .contact p { color: var(--dark-green); font-size: 6px; line-height: 8.2px; font-weight: 700; }
  .contact .office { margin-bottom: 7px; }
  .contact .group { margin-bottom: 5px; }
  .contact-rule { position: absolute; left: 145px; top: 71px; width: 1px; height: 158px; background: var(--line-blue); }

  /* cover visual */
  .cover-visual { position: absolute; left: 600px; top: 0; width: 600px; height: 400px;
    background:
      radial-gradient(ellipse 70% 25% at 55% 58%, rgba(120,190,255,0.85), transparent 70%),
      radial-gradient(ellipse 60% 40% at 80% 20%, rgba(70,150,240,0.7), transparent 70%),
      linear-gradient(180deg, #0a3a9c 0%, #0f5fd0 45%, #0b3f9f 75%, #082a72 100%); }
  .title-banner { position: absolute; left: 600px; top: 57px; width: 600px; height: 86px; background: var(--banner-black); }
  .title-line { position: absolute; font-size: 33px; white-space: nowrap; letter-spacing: 0.3px; }
  .title-line.first { left: 623px; top: 70px; color: var(--orange); }
  .title-line.second { left: 821px; top: 90px; color: var(--green); }
  .title-line.second .accent { color: var(--orange); }

  /* grey band */
  .band { position: absolute; left: 0; top: 414px; width: 1200px; height: 114px; background: var(--band-grey); }

  .brand { position: absolute; display: flex; align-items: flex-start; gap: 5px; }
  .brand-mark { background: var(--orange); flex: none; }
  .brand-name { color: #2e2e2e; line-height: 1.05; text-transform: uppercase; }
  .brand-sub { display: block; color: #b32020; text-transform: none; }

  .brand.back { left: 29px; top: 453px; }
  .brand.back .brand-mark { width: 22px; height: 22px; }
  .brand.back .brand-name { font-size: 11px; }
  .brand.back .brand-name small { font-size: 7.5px; display: block; }
  .brand.back .brand-sub { font-size: 4px; margin-top: 3px; }

  .brand.front { left: 632px; top: 450px; }
  .brand.front .brand-mark { width: 32px; height: 32px; }
  .brand.front .brand-name { font-size: 16px; }
  .brand.front .brand-name small { font-size: 10.5px; display: block; }
  .brand.front .brand-sub { font-size: 5.5px; margin-top: 4px; }

  .tagline { position: absolute; left: 877px; top: 463px; color: var(--navy); font-size: 16px; font-weight: 700; white-space: nowrap; }

  /* bottom strip */
  .next-page-visual { position: absolute; left: 600px; top: 543px; width: 600px; height: 57px;
    background: linear-gradient(120deg, #0c2556 0%, #16387a 50%, #0d2a62 100%); }
</style>
</head>
<body>
<main class="spread">

  <section class="contact">
    <h3>Address:</h3>
    <div class="office">
      <p># Dubai UAE</p>
      <p>P.O.Box : 204418, Dubai UAE</p>
      <p>Tel : +9714 5550172</p>
      <p>Fax : +9714 5550173</p>
    </div>
    <div class="office">
      <p># Sharjah, UAE</p>
      <p>P.O.Box : 61207, Sharjah UAE</p>
      <p>Tel : +9716 5550184</p>
      <p>Fax : +9716 5550185</p>
    </div>
    <div class="office group">
      <p>#Abu Dhabi, UAE</p>
      <p>P.O.Box : 73019, Abu Dhabi UAE</p>
      <p>Tel : +9712 5550196</p>
      <p>Fax : +9712 5550197</p>
    </div>
    <h3>Email ID:</h3>
    <div class="group"><p>hello@tovanelix.com</p></div>
    <h3>Website:</h3>
    <p>www.tovanelix.com</p>
  </section>
  <div class="contact-rule"></div>

  <div class="cover-visual" role="img" aria-label="Futuristic blue circuit-board landscape with glowing light streams"></div>
  <div class="title-banner"></div>
  <h1 class="title-line first">Innovative &amp;</h1>
  <h2 class="title-line second">Cost Effective <span class="accent">Solution</span></h2>

  <div class="band"></div>

  <div class="brand back">
    <span class="brand-mark"></span>
    <span class="brand-name">Tovane<small>Technologies L.L.C.</small>
      <span class="brand-sub">A Member of Tovane Group<br>Your Partner in Growth</span></span>
  </div>

  <div class="brand front">
    <span class="brand-mark"></span>
    <span class="brand-name">Tovane<small>Technologies L.L.C.</small>
      <span class="brand-sub">A Member of Tovane Group<br>Your Partner in Growth</span></span>
  </div>

  <p class="tagline">An Information &amp; Technologies Company</p>

  <div class="next-page-visual" role="img" aria-label="Dark blue technology texture"></div>
</main>
</body>
</html>
```